Psychology practice - information brochure/flyer - half A4 page folded (4 sides)

We need a brochure/flyer to market our psychology service to GPs (Doctors). We need to demonstrate to the doctors that we are the right choice for their patients, and that we cover a large range of services so all of their patients needs are met. We will demonstrate this by listing our range of services and our team of psychologists. We have two locations in Sydney and offer high end services. I've attached our company logo but we remain flexible regarding the style of the brochures. I will provide more details (services, locations & psychologist credentials) once our preferred brochure design has been selected.

```html
<!DOCTYPE html>
<html lang="en">
<head>
<meta charset="utf-8">
<title>Clear Path Clinical Psychology – Brochure Cover</title>
<link href="https://fonts.googleapis.com/css2?family=Arimo:wght@400;700&family=Josefin+Sans:wght@300&display=swap" rel="stylesheet">
<style>
  :root {
    --cream: #fbf5e6;
    --amber: #fbbf0e;
    --teal: #63c1cf;
    --charcoal: #2f2f2f;
    --grey: #6b6b6b;
    --orange: #f5a53a;
    --yellow: #fde21a;
    --white: #ffffff;
    --brand-ink: #4a4a4a;
  }
  html, body {
    margin: 0;
    padding: 0;
    overflow: hidden;
    background: var(--cream);
  }
  .cover {
    position: relative;
    width: 835px;
    height: 1200px;
    overflow: hidden;
    background: var(--cream);
  }
  .brand {
    position: absolute;
    top: 72px;
    left: 372px;
    display: flex;
    align-items: center;
    gap: 18px;
  }
  .brand-mark {
    width: 30px;
    height: 30px;
    background: var(--amber);
  }
  .brand-name {
    font-family: "Josefin Sans", sans-serif;
    font-weight: 300;
    color: var(--brand-ink);
    font-size: 56px;
    line-height: 1;
    margin: 0;
  }
  .brand-name span {
    display: block;
    font-size: 45px;
    line-height: 1.1;
  }
  .tagline-band {
    position: absolute;
    top: 313px;
    left: 0;
    width: 835px;
    height: 178px;
    background: var(--amber);
  }
  .tagline {
    position: absolute;
    top: 318px;
    left: 84px;
    margin: 0;
    font-family: "Arimo", sans-serif;
    font-weight: 400;
    font-size: 45px;
    line-height: 53px;
    color: var(--charcoal);
  }
  .tagline strong { font-weight: 700; }
  .stripes {
    position: absolute;
    top: 496px;
    left: 0;
  }
  .web-address {
    position: absolute;
    top: 503px;
    left: 413px;
    margin: 0;
    font-family: "Arimo", sans-serif;
    font-weight: 700;
    font-size: 18.5px;
    color: var(--charcoal);
  }
  .arcs {
    position: absolute;
    top: 0;
    left: 0;
  }
</style>
</head>
<body>
<main class="cover">
  <div class="brand">
    <div class="brand-mark"></div>
    <h1 class="brand-name">Clear Path<span>Clinical Psychology</span></h1>
  </div>

  <div class="tagline-band"></div>
  <h2 class="tagline">Working together<br>to <strong>achieve</strong> a <strong>better</strong><br>quality of <strong>life</strong></h2>

  <svg class="stripes" width="835" height="42" viewBox="0 0 835 42" aria-hidden="true">
    <rect x="0" y="0" width="835" height="16" fill="var(--teal)"/>
    <rect x="0" y="16" width="390" height="7" fill="var(--amber)"/>
    <polygon points="383,16 835,16 835,41 405,41" fill="var(--teal)"/>
  </svg>
  <p class="web-address">www.clearpathpsychology.com.au</p>

  <svg class="arcs" width="835" height="1200" viewBox="0 0 835 1200">
    <defs>
      <linearGradient id="arcWarm" x1="0" y1="0" x2="1" y2="0">
        <stop offset="0" stop-color="var(--yellow)"/>
        <stop offset="0.55" stop-color="#fbc21a"/>
        <stop offset="1" stop-color="var(--orange)"/>
      </linearGradient>
      <linearGradient id="photoTone" x1="0" y1="0" x2="1" y2="0">
        <stop offset="0" stop-color="#e4e0da"/>
        <stop offset="0.2" stop-color="#b79a7c"/>
        <stop offset="0.38" stop-color="#8c6f58"/>
        <stop offset="0.5" stop-color="#c9b7a0"/>
        <stop offset="0.66" stop-color="#f1ece4"/>
        <stop offset="0.85" stop-color="#e9e3da"/>
        <stop offset="1" stop-color="#d8cfc3"/>
      </linearGradient>
      <linearGradient id="photoShade" x1="0" y1="0" x2="0" y2="1">
        <stop offset="0" stop-color="#ffffff" stop-opacity="0.25"/>
        <stop offset="0.5" stop-color="#ffffff" stop-opacity="0"/>
        <stop offset="1" stop-color="#5a4436" stop-opacity="0.25"/>
      </linearGradient>
    </defs>
    <ellipse cx="440" cy="1330" rx="600" ry="720" fill="var(--grey)"/>
    <ellipse cx="455" cy="1345" rx="585" ry="690" fill="none" stroke="var(--white)" stroke-width="2"/>
    <ellipse cx="470" cy="1360" rx="570" ry="690" fill="url(#arcWarm)"/>
    <g role="img" aria-label="Photo: a psychologist listening to a client during a consultation in a bright office with bookshelves">
      <ellipse cx="470" cy="1400" rx="505" ry="705" fill="url(#photoTone)"/>
      <ellipse cx="470" cy="1400" rx="505" ry="705" fill="url(#photoShade)"/>
    </g>
  </svg>
</main>
</body>
</html>
```